Flyer Ballettschule
Vielen Dank für den wirklich sehr professionellen superschönen Flyer. Uns hat das Design beim ersten Entwurf schon perfekt gefallen. Sofort hat der Designer kleine Änderungen bestens umgesetzt. Sehr netter Kontakt. Ein ganz großes Dankeschön! Ballettschule Wendelmoor

```html
<!DOCTYPE html>
<html lang="de">
<head>
<meta charset="utf-8">
<title>Ballettschule Wendelmoor – Flyer</title>
<link rel="stylesheet" href="https://fonts.googleapis.com/css2?family=Crimson+Pro:wght@400;600;700&family=Cormorant+Garamond:ital,wght@1,500;1,600&display=swap">
<style>
  :root {
    --red: #e1201f;
    --charcoal: #4d4c4f;
    --section-grey: #eeeeee;
    --section-light: #f6f6f6;
    --text: #4a4a4a;
    --stage: #eeeeec;
  }
  * { box-sizing: border-box; margin: 0; padding: 0; }
  html, body { width: 1200px; height: 848px; overflow: hidden; }
  body {
    background: var(--stage);
    font-family: "Crimson Pro", Georgia, serif;
    color: var(--text);
    position: relative;
  }
  .flyer {
    position: absolute;
    left: 413px; top: 24px;
    width: 374px; height: 800px;
    background: var(--section-grey);
    overflow: hidden;
    box-shadow: 0 4px 14px rgba(0,0,0,.18);
  }
  .hero-photo {
    position: absolute; left: 0; top: 0; width: 374px; height: 167px;
    background: linear-gradient(100deg, #e7e5e3 0%, #f3f2f0 45%, #e9e7e5 100%);
  }
  .brand {
    position: absolute; left: 22px; top: 82px;
    display: flex; align-items: center; gap: 7px;
    font-size: 17px; font-weight: 600; color: var(--red);
  }
  .brand-dot { width: 10px; height: 10px; border-radius: 50%; background: var(--red); }
  .invite-band {
    position: absolute; left: 0; top: 167px; width: 374px; height: 86px;
    background: var(--charcoal);
    border-bottom: 1px dashed rgba(255,255,255,.35);
  }
  .invite-title {
    position: absolute; left: 21px; top: 22px;
    color: #fff; font-size: 18px; font-weight: 600; letter-spacing: .6px;
    line-height: 24px; text-transform: uppercase;
  }
  .anniversary {
    position: absolute; left: 293px; top: 158px; width: 70px; height: 112px;
  }
  .anniversary svg { position: absolute; inset: 0; }
  .anniversary-text {
    position: absolute; left: 0; top: 6px; width: 64px; text-align: center;
    color: #fff; font-family: "Cormorant Garamond", Georgia, serif; font-style: italic;
  }
  .anniversary-number { display: block; font-size: 40px; line-height: 38px; font-weight: 500; }
  .anniversary-word { display: block; font-size: 24px; line-height: 22px; font-weight: 600; }
  .anniversary-place { display: block; font-size: 10px; line-height: 16px; }
  .section-kids { position: absolute; left: 0; top: 253px; width: 374px; height: 220px; background: var(--section-grey); }
  .section-adults { position: absolute; left: 0; top: 473px; width: 374px; height: 165px; background: var(--section-light); }
  .section-contact { position: absolute; left: 0; top: 638px; width: 374px; height: 123px; background: var(--section-grey); }
  .dancer-art {
    position: absolute; left: 236px; top: 474px; width: 138px; height: 287px;
    background: radial-gradient(ellipse at 55% 45%, rgba(225,32,31,.55) 0%, rgba(225,32,31,.25) 55%, rgba(225,32,31,0) 80%);
  }
  .section-heading {
    position: absolute; left: 21px;
    color: var(--red); font-size: 13px; font-weight: 700; letter-spacing: .3px; text-transform: uppercase;
  }
  .course-list {
    position: absolute; left: 21px; list-style: none;
    font-size: 12.5px; font-weight: 600; line-height: 20.2px;
  }
  .course-list li { position: relative; padding-left: 25px; }
  .course-list li::before {
    content: ""; position: absolute; left: 0; top: 10px; width: 12px; height: 1.5px; background: #6a6a6a;
  }
  .course-list .course-note { display: block; font-size: 9.5px; line-height: 11px; margin-top: -3px; padding-bottom: 2px; }
  .contact-block {
    position: absolute; left: 21px; top: 9px;
    font-size: 11px; line-height: 15.3px;
  }
  .contact-name { color: var(--red); font-size: 13px; font-weight: 700; text-transform: uppercase; letter-spacing: .3px; line-height: 17px; }
  .site-footer {
    position: absolute; left: 0; top: 761px; width: 374px; height: 39px;
    background: var(--charcoal);
    color: #fff; font-size: 14px; font-weight: 600; letter-spacing: .8px;
    text-align: center; line-height: 39px; text-transform: uppercase;
  }
</style>
</head>
<body>
  <article class="flyer">
    <div class="hero-photo" role="img" aria-label="Foto: Beine von Ballettschülerinnen in hellen Strumpfhosen und Schläppchen an der Stange"></div>
    <div class="brand"><span class="brand-dot"></span><span>Ballettschule Wendelmoor</span></div>

    <header class="invite-band">
      <h1 class="invite-title">Herzliche Einladung<br>zu einer Probestunde</h1>
    </header>

    <div class="anniversary">
      <svg width="70" height="112" viewBox="0 0 70 112" aria-hidden="true">
        <polygon points="64,0 70,9 64,9" fill="#a3161a"/>
        <polygon points="0,0 64,0 64,112 32,100 0,112" fill="#e1201f"/>
      </svg>
      <div class="anniversary-text">
        <span class="anniversary-number">40</span>
        <span class="anniversary-word">Jahre</span>
        <span class="anniversary-place">in Pinneberg</span>
      </div>
    </div>

    <section class="section-kids">
      <h2 class="section-heading" style="top:20px">Kinder und Jugendliche</h2>
      <ul class="course-list" style="top:39px">
        <li>Tänzerische Früherziehung ab 3 Jahren</li>
        <li>Ballettvorbereitung ab 4 Jahren</li>
        <li>Klassisches Ballett ab 6 Jahren</li>
        <li>Klassisches Ballett mit Spitze ab 12 Jahren</li>
        <li>Jazz Tanz</li>
        <li>Step Tanz</li>
        <li>Hip Hop</li>
        <li>Berufsvorbereitung Tanz</li>
      </ul>
    </section>

    <section class="section-adults">
      <h2 class="section-heading" style="top:15px">Erwachsene</h2>
      <ul class="course-list" style="top:34px">
        <li>Klassisches Ballett<span class="course-note">(auch für Anfänger und Wiedereinsteiger)</span></li>
        <li>Jazz Tanz</li>
        <li>Step Tanz</li>
        <li>Flamenco</li>
        <li>Tänzerische Gymnastik 50+, 70+</li>
      </ul>
    </section>

    <section class="section-contact">
      <address class="contact-block" style="font-style:normal">
        <div class="contact-name">Ballettschule Wendelmoor</div>
        Inh. Marlene Wendelmoor<br>
        Lindenhofer Straße 14<br>
        25421 Pinneberg-Mitte<br>
        Telefon: 0 41 01 - 55 27 316<br>
        Mobil: 0 170 - 33 18 246<br>
        info@ballettschule-wendelmoor.de
      </address>
    </section>

    <div class="dancer-art" role="img" aria-label="Rote Silhouette einer Balletttänzerin im Tutu"></div>

    <footer class="site-footer">www.ballettschule-wendelmoor.de</footer>
  </article>
</body>
</html>
```